Product Insert / Thank You

I'm looking for a small card to be designed that will be included with our product when it ships. It will be 2 sided with 1 side being a "thank you" with our logo and the other side containing the following text:We would love to hear your feedback! For every review we receive on our products, we donate 100% of the proceeds of your order to TIDEWELL -- a non profit organization dedicated to preserving our oceans!If you are not 100% satisfied with your purchase or have any problems, we will always resolve your issue. please contact us via Brisko if you need assistance.Insert needs to be well organized and information presented in a clear and visually appealing way.
Target Market(s)
Women, aged 24-45
Colors
Designer to choose colors to be used in the design.
Look and feel
Each slider illustrates characteristics of the customer's brand and the style your logo design should communicate.

```html
<!DOCTYPE html>
<html lang="en">
<head>
<meta charset="utf-8">
<title>Product Insert – Feedback</title>
<link rel="stylesheet" href="https://fonts.googleapis.com/css2?family=Didact+Gothic&family=Kaushan+Script&display=swap">
<style>
  :root {
    --page-bg: #dcfad8;
    --disc: #6ff3b1;
    --ink: #000000;
    --ornament: #123a28;
  }
  html, body {
    margin: 0;
    padding: 0;
    width: 1200px;
    height: 1200px;
    overflow: hidden;
    background: var(--page-bg);
  }
  .insert {
    position: relative;
    width: 1200px;
    height: 1200px;
    background: var(--page-bg);
    color: var(--ink);
  }
  .insert__disc {
    position: absolute;
    left: 19px;
    top: 19px;
    width: 1162px;
    height: 1162px;
    border-radius: 50%;
    background: var(--disc);
  }
  .flourish {
    position: absolute;
    left: 466px;
    width: 271px;
    height: 90px;
    border-radius: 45px;
    background: var(--ornament);
    opacity: 0.85;
  }
  .flourish--top { top: 229px; }
  .flourish--bottom { top: 914px; }
  .headline,
  .signoff {
    position: absolute;
    left: 0;
    width: 1200px;
    margin: 0;
    text-align: center;
    font-family: "Kaushan Script", cursive;
    font-weight: 400;
    line-height: 1;
  }
  .headline {
    top: 372px;
    font-size: 46px;
  }
  .signoff {
    top: 815px;
    font-size: 42px;
  }
  .rule {
    position: absolute;
    left: 80px;
    width: 1034px;
    height: 2px;
    background: linear-gradient(to right, rgba(0,0,0,0), var(--ink) 12%, var(--ink) 88%, rgba(0,0,0,0));
  }
  .rule--upper { top: 447px; }
  .rule--lower { top: 796px; }
  .body-copy {
    position: absolute;
    left: 0;
    width: 1200px;
    top: 472px;
    margin: 0;
    text-align: center;
    font-family: "Didact Gothic", sans-serif;
    font-size: 25px;
    line-height: 34.5px;
  }
  .body-copy p { margin: 0; }
  .body-copy .charity { font-style: italic; }
  .body-copy .promise { margin-top: 35px; }
  .body-copy .divider-stars {
    font-weight: 700;
    letter-spacing: 4px;
    line-height: 26px;
  }
</style>
</head>
<body>
  <main class="insert">
    <div class="insert__disc"></div>

    <div class="flourish flourish--top" role="img" aria-label="Decorative black swirl flourish ornament"></div>

    <h1 class="headline">We would love to hear your feedback!</h1>
    <div class="rule rule--upper"></div>

    <div class="body-copy">
      <p>For every review we receive on our products,<br>
      we donate 100% of the proceeds of your order<br>
      to <span class="charity">TIDEWELL</span> - a non-profit organization dedicated to<br>
      preserving oceans!</p>
      <p class="promise">If you are not 100% satisfied with your purchase or<br>
      have any problems,<br>
      we will always resolve your issue.</p>
      <p class="divider-stars">* * *</p>
    </div>

    <div class="rule rule--lower"></div>
    <p class="signoff">Please contact us via Brisko if you need assistance.</p>

    <div class="flourish flourish--bottom" role="img" aria-label="Decorative black swirl flourish ornament"></div>
  </main>
</body>
</html>
```